Existing company needs Rebranding on logo and website!!

the company is called Harvest Bridge (www.harvestbridgefund.co.uk) check the site to see the existing site and logo, this has to change and must be completely different.

I want to the turn the website into a crowd funding site, but i want an inovative and interacive site. Have a look http://www.lendora.org/about/how or https://www.fundlarkly.com/ to get an idea of what is required. However i do not want my site to be anything like this. It is 2015 so web browser can do alot. when it comes to selecting project proposals on the site i want them them to pop up use your imagination your the desgner. ofcourse the site will be taking card payments and possibly bank transfers and maybe zentopay. the usual API are already on the site so you wont need to do much. the site is hosted by wordpress so i do prefer it to stay there. i am familiar with that platform.

interms of creativity you have full control we wil be working closely and i expect to be kept in the loop as things develope.

the site will also need to be turn into a mobile app which serves different purposes depending if your an investor or project sponsor.

i will give you all the information required we can communicate on chatvolt email or telephone i am flexible.

many thanks

Target Market(s)

Investors

Industry/Entity Type

Finance

Number of Pages Required

5+ page

Font styles to use
Sans Serif

Colors
3176b5
f04a50
abd036
00a990

Requirements
Must have
• i want the designer to look at my existing site www.harvestbridgefund.co.uk and come up with a better design concept.

```html
<!DOCTYPE html>
<html lang="en">
<head>
<meta charset="utf-8">
<title>Harvest Bridge – Brand and Homepage Concept</title>
<link rel="stylesheet" href="https://fonts.googleapis.com/css2?family=Ubuntu:wght@500;700&family=Open+Sans:wght@400;600&family=Arimo:wght@400&family=Montserrat:wght@700&display=swap">
<style>
  :root {
    --teal: #00a990;
    --coral: #f04a50;
    --blue: #3176b5;
    --lime: #abd036;
    --ink: #000000;
    --paper: #f5f7f8;
    --white: #ffffff;
    --panel: rgba(196, 196, 200, 0.9);
    --panel-ink: #111111;
  }
  * { margin: 0; padding: 0; box-sizing: border-box; }
  html, body { width: 885px; height: 1200px; overflow: hidden; background: var(--ink); }
  .canvas { position: relative; width: 885px; height: 1200px; background: var(--ink); overflow: hidden; }

  /* Logo presentation */
  .logo-board {
    position: absolute; left: 59px; top: 50px; width: 750px; height: 343px;
    background: radial-gradient(ellipse at 45% 40%, #ffffff 0%, var(--paper) 70%, #e9eef0 100%);
    display: flex; align-items: center; padding-left: 78px; gap: 26px;
  }
  .logo-board .mark-circle {
    width: 132px; height: 132px; border-radius: 50%;
    border: 12px solid var(--teal); flex: none;
  }
  .logo-board .wordmark {
    font-family: "Ubuntu", sans-serif; font-weight: 700; font-size: 50px;
    color: var(--teal); letter-spacing: 0.5px;
  }

  /* Website homepage */
  .site { position: absolute; left: 0; top: 416px; width: 885px; height: 784px; }
  .site-nav {
    position: absolute; left: 0; top: 0; width: 885px; height: 47px; background: var(--ink);
    border-top: 1px solid #222;
  }
  .site-nav .brand {
    position: absolute; left: 112px; top: 11px; display: flex; align-items: center; gap: 6px;
    font-family: "Ubuntu", sans-serif; font-weight: 500; font-size: 12px; color: var(--white);
  }
  .site-nav .brand .brand-dot {
    width: 24px; height: 24px; border-radius: 50%; border: 3px solid var(--teal);
  }
  .site-nav .menu { position: absolute; top: 17px; left: 0; list-style: none; font-family: "Open Sans", sans-serif; font-size: 9px; font-weight: 600; color: var(--white); }
  .site-nav .menu li { position: absolute; white-space: nowrap; }

  .hero-photo {
    position: absolute; left: 0; top: 47px; width: 885px; height: 416px;
    background:
      radial-gradient(ellipse at 38% 45%, #8a8c90 0%, #55575b 18%, rgba(20,20,22,0) 40%),
      radial-gradient(ellipse at 22% 85%, rgba(255,240,210,0.5) 0%, rgba(0,0,0,0) 12%),
      linear-gradient(180deg, #050505 0%, #0b0b0c 65%, #1d1e1f 100%);
  }
  .hero-panel {
    position: absolute; left: 489px; top: 166px; width: 396px; height: 297px;
    background: var(--panel); padding: 24px 0 0 43px; color: var(--panel-ink);
    font-family: "Arimo", sans-serif;
  }
  .hero-panel .hero-title { font-weight: 400; font-size: 26px; line-height: 27px; letter-spacing: -0.5px; }
  .hero-panel .hero-title strong { display: block; font-weight: 700; font-size: 36px; line-height: 36px; }
  .hero-panel .hero-lead { margin-top: 14px; font-size: 17px; letter-spacing: -0.3px; }
  .hero-panel .hero-list { list-style: none; margin-top: 10px; font-size: 17px; line-height: 21px; letter-spacing: -0.3px; }

  .accent-band { position: absolute; left: 0; top: 463px; width: 885px; height: 39px; background: var(--teal); }

  .services { position: absolute; left: 0; top: 502px; width: 885px; height: 201px; background: var(--coral); color: var(--white); }
  .services .services-title {
    position: absolute; left: 117px; top: 24px; font-family: "Montserrat", sans-serif; font-weight: 700;
    font-size: 34px; line-height: 34px; letter-spacing: -0.5px;
  }
  .services .services-title .underline { display: block; width: 205px; height: 4px; background: var(--white); margin-top: 4px; }
  .feature { position: absolute; width: 230px; height: 60px; }
  .feature .feature-icon {
    position: absolute; left: 0; top: 0; width: 56px; height: 56px; border-radius: 50%;
    border: 2px solid var(--white); display: flex; align-items: center; justify-content: center;
  }
  .feature h3 { position: absolute; left: 72px; top: 2px; font-family: "Open Sans", sans-serif; font-weight: 600; font-size: 9px; }
  .feature p { position: absolute; left: 72px; top: 16px; width: 150px; font-family: "Open Sans", sans-serif; font-size: 8px; line-height: 13px; }

  .icon-strip { position: absolute; left: 0; top: 703px; width: 885px; height: 81px; background: var(--white); }
  .icon-strip svg { position: absolute; top: 32px; }
</style>
</head>
<body>
<main class="canvas">

  <section class="logo-board" aria-label="Harvest Bridge logo">
    <span class="mark-circle"></span>
    <span class="wordmark">Harvest Bridge</span>
  </section>

  <section class="site" aria-label="Harvest Bridge homepage">
    <nav class="site-nav">
      <div class="brand"><span class="brand-dot"></span>Harvest Bridge</div>
      <ul class="menu">
        <li style="left:268px">Home</li>
        <li style="left:313px">About Us</li>
        <li style="left:368px">About Ghana</li>
        <li style="left:432px">Why Ghana</li>
        <li style="left:490px">Sponsorship</li>
        <li style="left:547px">News &amp; Media</li>
        <li style="left:617px">Contact Us</li>
      </ul>
    </nav>

    <div class="hero-photo" role="img" aria-label="Night photograph of a tall stone arch monument lit against a dark sky"></div>

    <div class="hero-panel">
      <h1 class="hero-title">HARVEST<strong>BRIDGE</strong></h1>
      <p class="hero-lead">Practical approach to doing business:</p>
      <ul class="hero-list">
        <li>&gt; Business &amp; Marketing Planning</li>
        <li>&gt; Investment Facilitation</li>
        <li>&gt; Business Guidance &amp; Support</li>
        <li>&gt; Feasibility Planning</li>
        <li>&gt; Business Development</li>
      </ul>
    </div>

    <div class="accent-band"></div>

    <section class="services">
      <h2 class="services-title">OUR<br>SERVICES.<span class="underline"></span></h2>

      <div class="feature" style="left:338px; top:24px">
        <span class="feature-icon">
          <svg width="24" height="16" viewBox="0 0 24 16"><path d="M6 15h13a4.5 4.5 0 0 0 0-9 6.5 6.5 0 0 0-12.4-1A5 5 0 0 0 6 15z" fill="#fff"/></svg>
        </span>
        <h3>FEATURE 1</h3>
        <p>Lorem ipsum dolor sit amet, consectetur adipisicing elit, sed do eiusmod.</p>
      </div>

      <div class="feature" style="left:560px; top:24px">
        <span class="feature-icon">
          <svg width="20" height="22" viewBox="0 0 20 22"><path d="M2 1v7a3 3 0 0 0 2.5 3V21h2V11A3 3 0 0 0 9 8V1H7.5v6h-1V1h-1v6h-1V1zM14 1c3 0 4 4 4 8h-2v12h-2z" fill="#fff"/></svg>
        </span>
        <h3>FEATURE 2</h3>
        <p>Lorem ipsum dolor sit amet, consectetur adipisicing elit, sed do eiusmod.</p>
      </div>

      <div class="feature" style="left:338px; top:112px">
        <span class="feature-icon">
          <svg width="14" height="22" viewBox="0 0 14 22"><path d="M9 1 2 12h5l-2 9 7-12H7z" fill="#fff"/></svg>
        </span>
        <h3>FEATURE 3</h3>
        <p>Incididunt ut labore et dolore magna aliqua. Ut enim ad minim veniam.</p>
      </div>

      <div class="feature" style="left:560px; top:112px">
        <span class="feature-icon">
          <svg width="22" height="22" viewBox="0 0 22 22"><g fill="#fff"><rect x="7" y="2" width="9" height="6" rx="1" transform="rotate(45 11.5 5)"/><rect x="2" y="12" width="10" height="3" transform="rotate(-45 7 13.5)"/></g></svg>
        </span>
        <h3>FEATURE 4</h3>
        <p>Incididunt ut labore et dolore magna aliqua. Ut enim ad minim veniam.</p>
      </div>
    </section>

    <div class="icon-strip">
      <svg style="left:156px" width="16" height="20" viewBox="0 0 16 20" fill="none" stroke="#3176b5" stroke-width="2"><path d="M8 2a5.5 5.5 0 0 0-3 10v3h6v-3A5.5 5.5 0 0 0 8 2z"/><path d="M5 18h6"/></svg>
      <svg style="left:265px" width="18" height="18" viewBox="0 0 18 18"><circle cx="9" cy="9" r="8" fill="#3176b5"/><path d="M5 4c2 1 1 3 3 4s0 3 2 5M12 3c-1 2 1 3 3 4" stroke="#fff" stroke-width="1.5" fill="none"/></svg>
      <svg style="left:374px" width="20" height="17" viewBox="0 0 20 17" fill="none" stroke="#3176b5" stroke-width="2"><rect x="1" y="3" width="18" height="13" rx="1"/><circle cx="10" cy="9.5" r="3.5"/><path d="M3 1h4"/></svg>
      <svg style="left:486px" width="19" height="19" viewBox="0 0 19 19"><path d="M2 17l8-8a4.5 4.5 0 0 1 6-6l-3 3 1.5 1.5 3-3a4.5 4.5 0 0 1-6 6l-8 8z" fill="#3176b5"/></svg>
      <svg style="left:598px" width="14" height="20" viewBox="0 0 14 20" fill="none" stroke="#3176b5" stroke-width="2"><rect x="4" y="1" width="6" height="11" rx="3" fill="#3176b5"/><path d="M1 9a6 6 0 0 0 12 0M7 15v4"/></svg>
      <svg style="left:706px" width="22" height="16" viewBox="0 0 22 16" fill="none" stroke="#3176b5" stroke-width="2"><rect x="1" y="1" width="20" height="14"/><circle cx="11" cy="8" r="3.5"/></svg>
    </div>
  </section>

</main>
</body>
</html>
```